New lease of life for a tired Country Pub menu, QLD

I need to refresh my menus with updated prices. The menus need to be A4 (the menus are laminated and handed out over the bar. I'd like to include our logo. I will upload our existing menus as well as the new prices. The design should be humble yet stylish if that's ok, please

Target Market(s)

Locals, travellers and workers

Industry/Entity Type

Hospitality, Quintessential Country pub

Font styles to use
Sans Serif

Colors

Designer to choose colors to be used in the design.

Requirements
Must have
• as we run different menus on different nights
Nice to have
• our logo

```html
<!DOCTYPE html>
<html lang="en">
<head>
<meta charset="utf-8">
<title>Hotel Dunmore – Lunch Menu</title>
<link rel="stylesheet" href="https://fonts.googleapis.com/css2?family=Fira+Sans+Condensed:wght@600;700&family=Montserrat:ital,wght@0,400;0,500;1,400&display=swap">
<style>
  :root {
    --backdrop: #999999;
    --card: #ffffff;
    --ink: #545454;
    --ink-soft: #4a4a4a;
    --on-ink: #ffffff;
  }
  * { margin: 0; padding: 0; box-sizing: border-box; }
  html, body { width: 890px; height: 1200px; overflow: hidden; }
  body { background: var(--backdrop); position: relative; font-family: "Montserrat", sans-serif; color: var(--ink); }

  .menu-card {
    position: absolute; left: 71px; top: 71px; width: 747px; height: 1057px;
    background: var(--card); border-radius: 27px; overflow: hidden;
    box-shadow: 10px 10px 12px rgba(0,0,0,0.28);
  }
  .header-arcs { position: absolute; left: 0; top: 0; width: 747px; height: 300px; }

  .brand-name {
    position: absolute; left: 0; right: 0; top: 60px; text-align: center;
    font-family: "Montserrat", sans-serif; font-weight: 500;
    font-size: 20px; line-height: 24px; letter-spacing: 0.5px; color: var(--ink);
  }
  .brand-name .brand-dot {
    display: inline-block; width: 10px; height: 10px; border-radius: 50%;
    background: var(--ink); margin-right: 9px; vertical-align: 2px;
  }

  .service-info {
    position: absolute; left: 0; right: 0; top: 184px; text-align: center;
    font-size: 13.5px; line-height: 16px; font-weight: 500; color: var(--ink-soft);
  }
  .service-info .hours { display: inline-block; background: var(--card); padding: 0 8px; font-size: 14px; }

  .menu-list { position: absolute; left: 0; right: 0; top: 248px; list-style: none; }
  .menu-item { position: relative; height: 74.3px; }
  .menu-item::before {
    content: ""; position: absolute; left: 0; top: 7px; width: 12px; height: 22px;
    background: var(--ink); border-radius: 0 3px 3px 0;
  }
  .item-name {
    position: absolute; left: 40px; top: 0; line-height: 37px;
    font-family: "Fira Sans Condensed", sans-serif; font-weight: 600;
    font-size: 28.4px; color: var(--ink); white-space: nowrap;
  }
  .item-desc {
    position: absolute; left: 41px; top: 34px; width: 475px;
    font-size: 11px; line-height: 14px; font-style: italic; color: var(--ink-soft);
  }
  .item-desc.wide { width: 600px; }
  .item-price {
    position: absolute; right: 0; top: 0; width: 139px; height: 37px;
    background: var(--ink); border-radius: 5px 0 0 5px;
    font-family: "Fira Sans Condensed", sans-serif; font-weight: 700;
    font-size: 34px; line-height: 37px; color: var(--on-ink); padding-left: 8px;
  }

  .footer-dome { position: absolute; left: 133px; bottom: 0; width: 483px; height: 70px; }
  .footer-note {
    position: absolute; left: 0; right: 0; bottom: 20px; text-align: center;
    font-family: "Fira Sans Condensed", sans-serif; font-weight: 600;
    font-size: 17.5px; line-height: 22px; color: var(--on-ink); letter-spacing: 0.3px;
  }
</style>
</head>
<body>
<main class="menu-card">
  <svg class="header-arcs" viewBox="0 0 747 300" aria-hidden="true">
    <path d="M5 14 Q 130 180 280 196" fill="none" stroke="#545454" stroke-width="5"/>
    <path d="M742 14 Q 617 180 467 196" fill="none" stroke="#545454" stroke-width="5"/>
    <path id="title-arc" d="M250 168 Q 373 200 496 168" fill="none"/>
    <text font-family="'Fira Sans Condensed', sans-serif" font-weight="700" font-size="45" fill="#545454" text-anchor="middle" letter-spacing="1">
      <textPath href="#title-arc" startOffset="50%">LUNCH MENU</textPath>
    </text>
  </svg>

  <div class="brand-name"><span class="brand-dot"></span>Hotel Dunmore</div>

  <div class="service-info">
    <span class="hours">Tuesday – Saturday 12-2pm</span><br>
    All burgers and wraps served with a side of chips
  </div>

  <ul class="menu-list">
    <li class="menu-item"><span class="item-name">CHICKEN BURGER AND CHIPS</span><p class="item-desc wide">Fried Harwood Butchery crumbed chicken thigh, cheese, tomato, spanish onion with aioli</p><span class="item-price">$19.99</span></li>
    <li class="menu-item"><span class="item-name">BEEF BURGER AND CHIPS</span><p class="item-desc">Grilled angus beef patty, lettuce, cheese, beetroot, tomato, spanish onion, pickles, caramelised onion with aioli</p><span class="item-price">$19.99</span></li>
    <li class="menu-item"><span class="item-name">STEAK BURGER AND CHIPS</span><p class="item-desc">Grilled Harwood Butchery rib fillet, lettuce, tomato, spanish onion, beetroot, cheese, caramelised onion with bbq sauce</p><span class="item-price">$21.00</span></li>
    <li class="menu-item"><span class="item-name">BARRAMUNDI BURGER AND CHIPS</span><p class="item-desc wide">Southern fried barramundi, lettuce, coleslaw with homemade dill and chives aioli</p><span class="item-price">$18.99</span></li>
    <li class="menu-item"><span class="item-name">CAESAR SALAD</span><p class="item-desc">Cos lettuce, croutons, parmesan cheese, boiled egg, caesar dressing</p><span class="item-price">$17.99</span></li>
    <li class="menu-item"><span class="item-name">CAESAR SALAD WITH CHICKEN</span><p class="item-desc">Cos lettuce, croutons, parmesan cheese, boiled egg, caesar dressing</p><span class="item-price">$21.00</span></li>
    <li class="menu-item"><span class="item-name">CAESAR SALAD WITH CALAMARI</span><p class="item-desc">Cos lettuce, croutons, parmesan cheese, boiled egg, caesar dressing</p><span class="item-price">$22.50</span></li>
    <li class="menu-item"><span class="item-name">CHICKEN CAESAR WRAP</span><span class="item-price">$19.00</span></li>
    <li class="menu-item"><span class="item-name">HONEY MUSTARD SALAD WITH CHICKEN</span><p class="item-desc wide">Mesclun mix, continental cucumber, cherry tomato, spanish onion, crispy chicken tenders (breast)</p><span class="item-price">$19.00</span></li>
    <li class="menu-item"><span class="item-name">BANGIN BURRITO</span><p class="item-desc">Minced beef, sliced beef sausage, rice, tomato puree, herbs</p><span class="item-price">$21.00</span></li>
  </ul>

  <svg class="footer-dome" viewBox="0 0 483 70" preserveAspectRatio="none" aria-hidden="true">
    <path d="M0 70 Q 241.5 -70 483 70 Z" fill="#545454"/>
  </svg>
  <p class="footer-note">HALF/ HALF NOT AVAILABLE</p>
</main>
</body>
</html>
```